Wellness Web Design Project

web design for business called Brightmoor Wellness. I have a private practice for which i need patients. I teach in house and online courses for professional and the public. It will be both an educational site as well as a marketing site and it will have a store and a member login area. I do sonic acupuncture called velarics. It is based on pythagoras' music of the spheres. I use vibrational and harmonic therapies to harmonize cells psyches and souls! it is the most scientifically rooted of the alternative therapies available and i focus on womens health, pediatric, emotional problems and spiritual awakening. I need it to be a balance of spiritual and symbolic depth as well as being graceful sophisticated grounded. I want it to look incredibly elegant, sophisticated, and established, not airy fairy! i like a minimal approach, fresh air, clean, confident, expensive, luxurious but also playful. im not trying to mold myself into the usual framework. i am trying to convey a sense of unleashing power and purpose and pleasure. i need it to be Gorgeous and relatable while being original
i have included the site map as an upload and here is a link to all the things that a home page should include. I have the logo and other versions that i will use to promote the different online programs i have. I may have a 'sound logo' start as the page comes up. the sounds are ethereal tones rather than music and super gentle and mysterious without being cloying or overly emotional. I work with the physical body, emotional trauma and altered states so many hats and have many different prongs to what i do so organization and clarity is important without getting cluttered. want to convert and capture into my email list for sure and have free downloadable content to provide.
the logo i have designed speaks volumes about my aesthetic. i have included a flyer made - which is 1. direction, but i am interested in seeing some designs that play with white space as well. the 'look' of the flyer has never been published and so am in no way married to it. I will include some of the photo i will want to use along the way that give you some sense of things or things to riff off. some of the photos of me have alot of solid blocks of color... i have included one of them. I am very sensitive to sophistication of color.
the site map i have included is jsut my attempt to organize - i am not married to it!
thankyou so much, and if you haven;t yet discovered the power of sound to alter brain waves and cell functioning wherever you are in the world - I highly recommend it:)

Target Market(s)

women 25-55's educated, familiar with alternative healing and conscious living who have money to spend on wellness

Industry/Entity Type

Business

Requirements
Must have
• http://notes.plimtrove.example/guides/4821/9 Core-Parts-Of-A-Good-Landing-Page-Chart.aspx
these are some of the elements that seem to be necessary
plus social media links....

```html
<!DOCTYPE html>
<html lang="en">
<head>
<meta charset="utf-8">
<title>Brightmoor Wellness</title>
<link href="https://fonts.googleapis.com/css2?family=Source+Sans+3:wght@300;400;600&display=swap" rel="stylesheet">
<style>
:root{
  --teal-deep:#0a5f78;
  --teal:#138a94;
  --green:#2f8a3a;
  --green-dark:#1f6a2c;
  --orange:#f29a2a;
  --orange-text:#d9821c;
  --gold:#f2b43a;
  --ink:#555;
  --ink-dark:#333;
  --hero:#4a4a4a;
  --footer:#1d2a33;
  --line:#ddd;
}
*{box-sizing:border-box;margin:0;padding:0}
html,body{width:978px;height:1200px;overflow:hidden}
body{font-family:"Source Sans 3",sans-serif;color:var(--ink);position:relative;
  background:
    radial-gradient(ellipse 520px 420px at 480px 760px,#fff 55%,rgba(255,255,255,0) 100%),
    radial-gradient(ellipse 300px 200px at 780px 1060px,rgba(240,230,140,.55),rgba(240,230,140,0)),
    linear-gradient(90deg,var(--teal-deep) 0%,var(--teal) 20%,#5fb8a8 50%,var(--teal) 80%,var(--teal-deep) 100%);}
.abs{position:absolute}
.top-band{left:0;top:0;width:978px;height:16px;background:linear-gradient(90deg,#12806f,var(--teal-deep))}
.header{left:0;top:16px;width:978px;height:121px;background:#fff}
.brand{left:98px;top:50px;display:flex;align-items:center;gap:12px}
.brand-mark{width:44px;height:44px;border-radius:50%;background:var(--gold)}
.brand-name{font-size:24px;font-weight:400;color:var(--green);letter-spacing:1.5px;text-transform:uppercase}
.contact-top{left:685px;top:34px;font-size:14px;font-weight:600;color:var(--green);line-height:25px}
.contact-top span{color:var(--orange);font-weight:400}
.search{left:691px;top:92px;width:145px;height:30px;border:1px solid #ccc;border-radius:3px;background:#fff;font-size:11px;color:#444;padding:7px 12px;box-shadow:0 1px 3px rgba(0,0,0,.12)}
.search svg{position:absolute;right:8px;top:6px}
.go{left:843px;top:92px;width:34px;height:30px;background:#36b34a;border-radius:3px;color:#fff;font-size:14px;text-align:center;line-height:30px}
.nav{left:0;top:137px;width:978px;height:38px;background:var(--green);display:block}
.nav a{position:absolute;top:0;height:38px;line-height:38px;color:#fff;font-size:12.5px;text-decoration:none;text-transform:uppercase}
.nav .active{background:var(--orange);width:90px;text-align:center}
.hero{left:87px;top:184px;width:804px;height:275px;background:var(--hero);box-shadow:0 8px 12px rgba(0,0,0,.25)}
.hero-photo{left:0;top:0;width:330px;height:275px;background:linear-gradient(135deg,#8a8a8a,#5a5a5a 60%,var(--hero))}
.hero h1{left:61px;top:68px;font-size:21px;font-weight:300;color:var(--gold);line-height:26px}
.hero p{left:61px;top:131px;width:339px;font-size:11.5px;line-height:18px;color:#fff;text-align:justify}
.btn-book{left:61px;top:196px;width:212px;height:35px;background:var(--orange);border-radius:3px;color:#fff;font-size:16px;font-weight:300;text-align:center;line-height:35px;box-shadow:0 2px 3px rgba(0,0,0,.3)}
.dots{left:37px;top:248px;display:flex;gap:7px}
.dots i{width:11px;height:11px;border-radius:50%;background:#fff}
.video{left:438px;top:38px;width:344px;height:228px;background:#888;padding:5px}
.video-frame{width:100%;height:100%;background:linear-gradient(135deg,#6d7a55,#b59a7a 50%,#3f4a38)}
.video .bar{left:15px;top:204px;width:295px;height:4px;background:#bbb}
.play{left:248px;top:97px}
h2.section{font-size:21px;font-weight:400;color:var(--orange-text)}
.welcome{left:92px;top:482px}
.welcome-text{left:92px;top:516px;width:554px;font-size:11px;line-height:18px;color:#4a4a4a}
.btn-green{background:linear-gradient(#2f8f45,var(--green-dark));border-radius:3px;color:#fff;font-size:12px;text-align:center;text-transform:uppercase;box-shadow:0 1px 2px rgba(0,0,0,.3)}
.panel{width:267px;height:321px;top:650px;background:linear-gradient(#fff 70%,#eee);border:1px solid #e2e2e2;border-radius:3px}
.panel-head{height:48px;background:linear-gradient(#f7b14a,var(--orange));color:#fff;font-size:15px;padding:18px 22px;text-transform:uppercase}
.item{position:absolute;left:12px;width:241px}
.item h3{font-size:10.8px;line-height:14px;font-weight:400;color:var(--orange-text);text-transform:uppercase}
.item p{font-size:10.8px;line-height:17px;color:#666;margin-top:4px;padding-bottom:8px;border-bottom:1px solid var(--line)}
.item.last p{border-bottom:none;padding-bottom:0}
.side-box{left:672px;width:215px;background:#fff;border:1px solid #e2e2e2;border-radius:3px}
.side-box h2{font-size:15px;font-weight:400;color:var(--green);margin:7px 0 0 12px}
.tvideo{left:17px;top:33px;width:180px;height:141px;background:linear-gradient(160deg,#5c6b3f,#a08a76 55%,#2c2c2c)}
.tvideo .cap{position:absolute;left:0;top:0;width:100%;height:18px;background:rgba(0,0,0,.85);color:#fff;font-size:10px;padding:3px 10px}
.socials{left:17px;top:184px;display:flex;gap:9px}
.socials i{width:22px;height:22px;border-radius:2px;background:#3a6fb0}
.velarics{background:linear-gradient(#fff,#e7eef2)}
.velarics .q{left:12px;top:12px;font-size:12px;line-height:15px;color:var(--ink-dark)}
.velarics .dl{left:12px;top:45px;font-size:11.5px;line-height:15px;color:var(--green)}
.velarics .dl b{font-weight:400;color:#444;font-size:13px}
.btn-dl{left:13px;top:78px;width:145px;height:27px;line-height:27px;font-weight:600;font-size:11.5px}
.btn-dl em{position:absolute;right:10px;top:6px;width:15px;height:15px;border-radius:50%;background:rgba(255,255,255,.35)}
.pdf{left:170px;top:64px;width:32px;height:38px;background:#f4f4f4;border:1px solid #ccc;border-radius:2px}
.resources h2{color:var(--green-dark);text-transform:uppercase}
.resources .awards{left:8px;top:36px;font-size:11.5px;color:#555}
.badge{top:58px;height:56px}
.footer-h{font-size:22px;font-weight:300;color:#444}
.input{left:97px;top:1033px;width:226px;height:28px;background:#fff;border-radius:14px;font-size:10.5px;color:#666;padding:7px 0 0 36px}
.input svg{position:absolute;left:11px;top:8px}
.sub-note{left:196px;top:1072px;font-size:10.5px;color:#fff}
.btn-sub{left:232px;top:1096px;width:87px;height:28px;background:var(--orange);border-radius:3px;color:#fff;font-size:13px;font-weight:600;text-align:center;line-height:28px}
.ci{font-size:11px;color:#fff}
.ci svg{position:absolute;left:-18px;top:1px}
.map{left:667px;top:1003px;width:229px;height:97px;border:2px solid #ddd;background:linear-gradient(135deg,#e9e4d8,#d8e2cc 50%,#efe8d4)}
.round{top:1117px;width:25px;height:25px;border-radius:50%;background:#e8eef0;opacity:.9}
.footer{left:0;top:1152px;width:978px;height:48px;background:var(--footer)}
.footer a{position:absolute;top:18px;font-size:10.5px;color:#fff;text-decoration:none}
.copy{left:678px;top:22px;font-size:9px;color:#bbb}
</style>
</head>
<body>
<div class="abs top-band"></div>
<header class="abs header"></header>
<div class="abs brand"><span class="brand-mark"></span><span class="brand-name">Brightmoor Wellness</span></div>
<div class="abs contact-top">Call Us : <span>310-555-0148</span><br>Email Us : <span>hello@brightmoorwellness.example</span></div>
<div class="abs search">Search
  <svg width="18" height="18" viewBox="0 0 18 18"><circle cx="7" cy="7" r="5" fill="none" stroke="#bbb" stroke-width="2"/><line x1="11" y1="11" x2="16" y2="16" stroke="#bbb" stroke-width="2.5"/></svg>
</div>
<div class="abs go">GO</div>
<nav class="abs nav">
  <a class="active" style="left:93px">Home</a>
  <a style="left:204px">Services</a>
  <a style="left:296px">Testimonials</a>
  <a style="left:417px">Features</a>
  <a style="left:513px">Videos</a>
  <a style="left:597px">News</a>
  <a style="left:672px">Contact Us</a>
</nav>

<section class="abs hero">
  <div class="abs hero-photo" role="img" aria-label="Greyscale photo of a practitioner applying tuning forks during a treatment"></div>
  <h1 class="abs">We do Sonic Acupunture and<br>we call it as VELARICS</h1>
  <p class="abs">Pellentesque eget justo sapien. Suspendisse vulputate erat ut erat molestie eget euismod diam porta. Cras ullamcorper sapien eget nisi tempus adipiscing. Phasellus fringilla, felis eu.</p>
  <div class="abs btn-book">BOOK APPOINTMENT NOW</div>
  <div class="abs dots"><i></i><i></i><i></i><i></i></div>
  <div class="abs video">
    <div class="video-frame" role="img" aria-label="Video still of the practitioner speaking outdoors"></div>
    <div class="abs bar"></div>
    <svg class="abs play" width="34" height="40" viewBox="0 0 34 40"><polygon points="0,0 34,20 0,40" fill="#fff" opacity=".9"/></svg>
  </div>
</section>

<h2 class="abs section welcome">Welcome to our website</h2>
<p class="abs welcome-text">Maecenas vel odio ac urna viverra dapibus vel vitae augue. Quisque eros neque, tincidunt id adipiscing ut, congue et tortor. Ut vel aliquam felis. Nulla facilisi. Donec pretium leo quis libero porttitor quis posuere sem rhoncus. Integer scelerisque urna et ante commodo elementum. Donec rhoncus dignissim urna, eu convallis dolor convallis in. Praesent euismod neque dui, vel scelerisque lectus. Morbi et nisl dolor, eu tempus dolor. Quisque dui mauris, luctus in faucibus a, fermentum eu odio. Nulla facilisi. Duis a nisi ut urna bibendum elementum non id nunc.</p>
<div class="abs btn-green" style="left:92px;top:611px;width:86px;height:28px;line-height:28px">View More</div>

<section class="abs panel" style="left:93px">
  <div class="panel-head">Features</div>
  <div class="item" style="top:64px"><h3>Lorem Ipsum is simply dummy text&nbsp; printing</h3><p>Lorem Ipsum is simply dummy text of the printing and typesetting industry. Lorem Ipsum has been.</p></div>
  <div class="item" style="top:140px"><h3>Lorem Ipsum is simply dummy text&nbsp; printing</h3><p>Lorem Ipsum is simply dummy text of the printing and typesetting industry.</p></div>
  <div class="item last" style="top:214px"><h3>Lorem Ipsum is simply dummy text&nbsp; printing</h3><p>Lorem Ipsum is simply dummy text of the printing and typesetting industry. Lorem Ipsum has been.</p></div>
  <div class="abs btn-green" style="left:10px;top:278px;width:144px;height:27px;line-height:27px">View More Features</div>
</section>
<section class="abs panel" style="left:378px">
  <div class="panel-head">Latest News</div>
  <div class="item" style="top:64px"><h3>Lorem Ipsum is simply dummy text&nbsp; printing</h3><p>Lorem Ipsum is simply dummy text of the printing and typesetting industry. Lorem Ipsum has been.</p></div>
  <div class="item" style="top:140px"><h3>Lorem Ipsum is simply dummy text&nbsp; printing</h3><p>Lorem Ipsum is simply dummy text of the printing and typesetting industry.</p></div>
  <div class="item last" style="top:214px"><h3>Lorem Ipsum is simply dummy text&nbsp; printing</h3><p>Lorem Ipsum is simply dummy text of the printing and typesetting industry. Lorem Ipsum has been.</p></div>
  <div class="abs btn-green" style="left:12px;top:276px;width:127px;height:27px;line-height:27px">View More News</div>
</section>

<aside class="abs side-box" style="top:480px;height:215px">
  <h2>Testimonials/Reviews</h2>
  <div class="abs tvideo" role="img" aria-label="Testimonial video still of a client speaking in a studio">
    <div class="cap">Verdant Path Studio</div>
    <svg class="abs" style="left:72px;top:59px" width="36" height="24" viewBox="0 0 36 24"><rect width="36" height="24" rx="5" fill="#111" opacity=".85"/><polygon points="14,6 24,12 14,18" fill="#fff"/></svg>
  </div>
  <div class="abs socials"><i></i><i style="background:#3fb3e6"></i><i style="background:#333"></i><i style="background:#f39a1d"></i><i style="background:#c9261f"></i><i style="background:#8aa3b3"></i></div>
</aside>

<aside class="abs side-box velarics" style="top:703px;height:110px">
  <p class="abs q">Want to know moreabout Velarics?<br>Know how it works?</p>
  <p class="abs dl">Then download our <b>FREE PDF</b><br>description</p>
  <div class="abs btn-green btn-dl">Download Now<em></em></div>
  <div class="abs pdf"></div>
</aside>

<aside class="abs side-box resources" style="top:822px;height:146px">
  <h2>View Our Resources</h2>
  <p class="abs awards">Awards</p>
  <div class="abs badge" style="left:8px;width:58px;background:#f2c23a;border-radius:4px"></div>
  <div class="abs badge" style="left:78px;width:62px;background:#2f5fb0;border-radius:50%"></div>
  <div class="abs badge" style="left:150px;width:58px;background:#3d9ac8;border-radius:50%"></div>
</aside>

<h2 class="abs footer-h" style="left:101px;top:996px">News Letter</h2>
<div class="abs input">
  <svg width="18" height="13" viewBox="0 0 18 13"><rect x="1" y="1" width="16" height="11" fill="none" stroke="#777" stroke-width="1.5"/><polyline points="1,1 9,7 17,1" fill="none" stroke="#777" stroke-width="1.5"/></svg>
  Subscribe your news letter
</div>
<p class="abs sub-note">Subscribe your news letter</p>
<div class="abs btn-sub">Subscribe</div>

<h2 class="abs footer-h" style="left:387px;top:996px">Contact info.</h2>
<div class="abs ci" style="left:403px;top:1039px">
  <svg width="12" height="11" viewBox="0 0 12 11"><polygon points="6,0 12,5 10,5 10,11 2,11 2,5 0,5" fill="#fff"/></svg>42 Fernhollow Rd</div>
<div class="abs ci" style="left:403px;top:1064px">Ashbury</div>
<div class="abs ci" style="left:403px;top:1089px">Oregon 970210</div>
<div class="abs ci" style="left:517px;top:1039px">
  <svg width="11" height="11" viewBox="0 0 11 11"><path d="M2 0l2 3-1.2 1.2a6 6 0 003.6 3.6L7.6 6.6l3 2-1.5 2.4C4.5 11 0 6.5 0 1.5z" fill="#fff"/></svg>+1 800 555 0192</div>
<div class="abs ci" style="left:517px;top:1064px">
  <svg width="10" height="12" viewBox="0 0 10 12"><path d="M0 0h7l3 3v9H0z" fill="#fff"/></svg>+1 504 555 0177</div>
<div class="abs ci" style="left:517px;top:1089px">
  <svg width="12" height="9" viewBox="0 0 12 9"><rect x=".5" y=".5" width="11" height="8" fill="none" stroke="#fff"/><polyline points=".5,.5 6,5 11.5,.5" fill="none" stroke="#fff"/></svg>mail@brightmoor.example</div>

<div class="abs map" role="img" aria-label="Street map showing the clinic location"></div>
<i class="abs round" style="left:733px"></i>
<i class="abs round" style="left:767px"></i>
<i class="abs round" style="left:801px"></i>
<i class="abs round" style="left:835px"></i>
<i class="abs round" style="left:868px"></i>

<footer class="abs footer">
  <a style="left:93px">Home</a>
  <a style="left:135px">About Us</a>
  <a style="left:193px">Our Services</a>
  <a style="left:270px">Testimonials</a>
  <a style="left:344px">Features</a>
  <a style="left:400px">Videos</a>
  <a style="left:452px">News</a>
  <a style="left:503px">Contact Us</a>
  <span class="abs copy">©brightmoorwellness.com 2013, All Rights Reserved</span>
</footer>
</body>
</html>
```